Window graphics for Kneadful Haven

We need a new look for our store front. Attached is the current look and two samples of our logo.
the window measurements are (WxH in inches)
Top left: 72x32.5, each of the doors: 30x75.5, verical narrow window: 25.25x101, each of the two large windows on the right: 72x101

The new look will need to included the following content:

Content in each window:

Top left window: Our logo + 3172 (for the logo, try both short and long style)

Bottom left door: 555-203-7184 (don't make it too large. It must look clean and professional)

Right door: Logo

Vertical window right of right door: Every Day 10-9

Left large window:
Walk-Ins Welcome
Give the Gift of Massage!

Right large window:
Couples Massage
Hot Stone & Deep Tissue
Swedish & Foot

Target Market(s)

70% women, 30% men, middle class

Industry/Entity Type

Massage Center

Requirements
Must have
• A new fresh look to our store front. Easily read from a distance. The graphics and text must all be white only
Nice to have
• A clean look. See attached picture of a barber shop in our area.
Should not have
• Covering of whole window. Our landlord will not allow it.

```html
<!DOCTYPE html>
<html lang="en">
<head>
<meta charset="utf-8">
<title>Kneadful Haven – Window Graphics</title>
<link href="https://fonts.googleapis.com/css2?family=Archivo+Black&family=Arimo:wght@400;700&display=swap" rel="stylesheet">
<style>
  :root {
    --bg: #000000;
    --ink: #ffffff;
    --frame: #d9d9d9;
    --rule: #6a6a6a;
  }
  * { margin: 0; padding: 0; box-sizing: border-box; }
  html, body { width: 1200px; height: 2400px; overflow: hidden; background: var(--bg); }
  .canvas { position: relative; width: 1200px; height: 2400px; background: var(--bg); color: var(--ink); }

  .label { position: absolute; text-align: center; font-family: "Arimo", Arial, sans-serif; font-weight: 400; font-size: 28px; line-height: 33px; color: var(--ink); }
  .label--bold { font-weight: 700; font-size: 19px; line-height: 22px; }

  .pane { position: absolute; border: 1.5px solid var(--frame); }
  .pane--open-bottom { border-bottom: none; }

  .block { position: absolute; left: 0; right: 0; text-align: center; font-family: "Archivo Black", "Arial Black", sans-serif; color: var(--ink); }

  .brand { font-size: 56px; line-height: 60px; letter-spacing: 0.5px; white-space: nowrap; }
  .brand--stack { font-size: 46px; line-height: 46px; }
  .brand--door { font-size: 36px; line-height: 36px; }

  .rule { position: absolute; left: 29px; right: 29px; height: 2px; background: linear-gradient(90deg, transparent, var(--rule) 15%, var(--rule) 85%, transparent); }
  .address { font-size: 21px; line-height: 26px; letter-spacing: 0.3px; white-space: nowrap; }

  .phone-num, .hours { font-size: 33px; line-height: 37.5px; letter-spacing: 1px; }
  .headline { font-size: 42px; line-height: 54px; letter-spacing: 2px; }
  .services { font-size: 40px; line-height: 51.2px; letter-spacing: 2px; }

  .icon { position: absolute; }
  .badge { position: absolute; width: 72px; height: 72px; border-radius: 50%; background: var(--ink); }
</style>
</head>
<body>
<main class="canvas">

  <!-- Top left window -->
  <p class="label label--bold" style="left:0;width:1200px;top:85px;">Top Left Window</p>

  <section class="pane" style="left:325px;top:138px;width:549px;height:215px;">
    <div class="block brand" style="top:56px;">Kneadful Haven</div>
    <div class="rule" style="top:143px;"></div>
    <div class="block address" style="top:162px;">3172 E Linden Ave. Brookfield, OH, US 44099</div>
  </section>

  <section class="pane" style="left:325px;top:399px;width:549px;height:215px;">
    <div class="block brand brand--stack" style="top:30px;">Kneadful<br>Haven</div>
    <div class="rule" style="top:163px;"></div>
    <div class="block address" style="top:174px;">3172 E Linden Ave. Brookfield, OH, US 44099</div>
  </section>

  <!-- Doors & narrow window -->
  <p class="label" style="left:80px;width:268px;top:719px;">Left Door</p>
  <p class="label" style="left:491px;width:267px;top:719px;">Right Door</p>
  <p class="label" style="left:862px;width:250px;top:702px;">Verical Narrow<br>Window</p>

  <section class="pane door-panel" style="left:80px;top:802px;width:268px;height:324px;">
    <svg class="icon" style="left:99px;top:65px;" width="70" height="68" viewBox="0 0 70 68" aria-hidden="true">
      <path d="M14 6 L24 4 L30 20 L23 26 Q28 40 39 47 L45 40 L60 47 L58 57 Q50 66 38 61 Q14 49 6 24 Q4 12 14 6 Z" fill="#fff"/>
      <path d="M40 22 Q47 24 49 31" stroke="#fff" stroke-width="4" fill="none" stroke-linecap="round"/>
      <path d="M42 12 Q56 15 59 29" stroke="#fff" stroke-width="4" fill="none" stroke-linecap="round"/>
      <path d="M44 2 Q65 6 68 27" stroke="#fff" stroke-width="4" fill="none" stroke-linecap="round"/>
    </svg>
    <div class="block phone-num" style="top:155px;">555<br>- 203 -<br>7184</div>
  </section>
  <section class="pane" style="left:80px;top:1130px;width:268px;height:324px;"></section>

  <section class="pane" style="left:491px;top:802px;width:267px;height:324px;">
    <div class="block brand brand--door" style="top:141px;">Kneadful<br>Haven</div>
  </section>
  <section class="pane" style="left:491px;top:1130px;width:267px;height:324px;"></section>

  <section class="pane pane--open-bottom" style="left:902px;top:797px;width:169px;height:659px;">
    <svg class="icon" style="left:50px;top:236px;" width="68" height="76" viewBox="0 0 68 76" aria-hidden="true">
      <rect x="28" y="1" width="12" height="4" fill="#fff"/>
      <rect x="32" y="4" width="4" height="6" fill="#fff"/>
      <circle cx="34" cy="41" r="30" fill="none" stroke="#fff" stroke-width="3.5"/>
      <line x1="34" y1="41" x2="34" y2="22" stroke="#fff" stroke-width="2.5"/>
      <line x1="34" y1="41" x2="50" y2="41" stroke="#fff" stroke-width="2.5"/>
      <line x1="14" y1="64" x2="8" y2="73" stroke="#fff" stroke-width="3.5" stroke-linecap="round"/>
      <line x1="54" y1="64" x2="60" y2="73" stroke="#fff" stroke-width="3.5" stroke-linecap="round"/>
    </svg>
    <div class="block hours" style="top:328px;">EVERY<br>DAY<br>10-9</div>
  </section>

  <!-- Large windows -->
  <p class="label" style="left:80px;width:477px;top:1547px;">Left Large<br>Windows</p>
  <p class="label" style="left:642px;width:477px;top:1547px;">Right Large<br>Windows</p>

  <section class="pane" style="left:80px;top:1639px;width:477px;height:677px;">
    <div class="badge" style="left:116px;top:121px;" role="img" aria-label="Rolled towels icon"></div>
    <div class="badge" style="left:203px;top:121px;" role="img" aria-label="Bamboo icon"></div>
    <div class="badge" style="left:289px;top:121px;" role="img" aria-label="Mortar and flower icon"></div>
    <div class="block headline" style="top:217px;">WALK-INS<br>WELCOME<br>GIVE THE<br>GIFT OF<br>MASSAGE!</div>
    <div class="badge" style="left:120px;top:514px;" role="img" aria-label="Stacked stones icon"></div>
    <div class="badge" style="left:203px;top:514px;" role="img" aria-label="Spa beauty icon"></div>
    <div class="badge" style="left:286px;top:514px;" role="img" aria-label="Lotus icon"></div>
  </section>

  <section class="pane" style="left:642px;top:1639px;width:477px;height:677px;">
    <div class="badge" style="left:115px;top:93px;" role="img" aria-label="Foot massage icon"></div>
    <div class="badge" style="left:202px;top:93px;" role="img" aria-label="Massage table icon"></div>
    <div class="badge" style="left:290px;top:93px;" role="img" aria-label="Couples massage icon"></div>
    <div class="block services" style="top:183px;">COUPLES<br>MASSAGE<br>HOT STONE &amp;<br>DEEP TISSUE<br>SWEDISH &amp;<br>FOOT</div>
    <div class="badge" style="left:115px;top:514px;" role="img" aria-label="Candle icon"></div>
    <div class="badge" style="left:202px;top:514px;" role="img" aria-label="Hot stones and towels icon"></div>
    <div class="badge" style="left:290px;top:514px;" role="img" aria-label="Back massage icon"></div>
  </section>

</main>
</body>
</html>
```